Brightmoor Card Company Business Cards

We are a trading card store with Zorblix, sports and other TCG cards, we need a business card design that encompasses a clean cut, modern style with a retro flare. website is brightmoorcardco.com for reference. Can utilize a comic book era feel or a more modern outdoor feel to utilize the "Pacific Northwest" elements of tress, mountains, etc.

Industry/Entity Type

Trading cards and collectibles

Contact Information for Business Card

business name, email address, phone number, name, owner job title

Font styles to use
Sans Serif

```html
<!DOCTYPE html>
<html lang="en">
<head>
<meta charset="utf-8">
<title>Brightmoor Card Company – Business Cards</title>
<link rel="stylesheet" href="https://fonts.googleapis.com/css2?family=Montserrat:wght@400;500;700;800&display=swap">
<style>
  :root {
    --stage: #2b2b2b;
    --cyan: #10bee0;
    --cyan-deep: #079fc0;
    --white: #ffffff;
    --ink: #1f1f1f;
    --grey: #6a6a6a;
  }
  * { box-sizing: border-box; margin: 0; padding: 0; }
  html, body {
    width: 1200px; height: 689px; overflow: hidden;
    background: var(--stage);
    font-family: "Montserrat", sans-serif;
  }
  .sheet {
    width: 1200px; height: 689px;
    display: flex; align-items: center; justify-content: center; gap: 50px;
  }
  .card {
    width: 540px; height: 310px; border-radius: 22px;
    position: relative; overflow: hidden;
  }
  /* Front */
  .card-front { background: var(--cyan); display: flex; align-items: center; justify-content: center; }
  .front-brand {
    display: flex; flex-direction: column; align-items: center; gap: 12px;
  }
  .front-brand .mark-square {
    width: 34px; height: 34px; background: var(--cyan-deep);
  }
  .front-brand .brand-name {
    color: var(--cyan-deep); font-weight: 800; font-size: 28px;
    letter-spacing: 1.5px; text-transform: uppercase; text-align: center; line-height: 1.15;
  }
  /* Back */
  .card-back { background: var(--white); display: flex; align-items: center; padding: 0 34px 0 30px; }
  .back-brand {
    width: 200px; display: flex; flex-direction: column; align-items: center; gap: 10px;
  }
  .back-brand .mark-square { width: 28px; height: 28px; background: var(--cyan); }
  .back-brand .brand-name {
    color: var(--grey); font-weight: 800; font-size: 20px;
    text-transform: uppercase; text-align: center; line-height: 1.2; letter-spacing: 1px;
  }
  .divider { width: 2px; height: 190px; background: var(--cyan); margin: 0 24px 0 18px; }
  .details { color: var(--ink); }
  .person-name { color: var(--cyan); font-weight: 800; font-size: 26px; letter-spacing: 0.5px; }
  .person-title { font-size: 14px; margin-top: 2px; }
  .region { color: var(--cyan); font-size: 14px; margin-top: 14px; }
  .address { font-size: 14px; }
  .contact-list { list-style: none; margin-top: 14px; }
  .contact-list li { display: flex; align-items: center; gap: 8px; font-size: 14px; line-height: 1.55; }
  .contact-list svg { width: 12px; height: 12px; fill: var(--cyan); flex: none; }
</style>
</head>
<body>
<main class="sheet">
  <section class="card card-front" aria-label="Card front">
    <div class="front-brand">
      <span class="mark-square"></span>
      <span class="brand-name">Brightmoor<br>Card Company</span>
    </div>
  </section>

  <section class="card card-back" aria-label="Card back">
    <div class="back-brand">
      <span class="mark-square"></span>
      <span class="brand-name">Brightmoor<br>Card Company</span>
    </div>
    <div class="divider"></div>
    <div class="details">
      <p class="person-name">DANIEL REYES</p>
      <p class="person-title">Managing Director</p>
      <p class="region">Pacific Northwest</p>
      <p class="address">Your address, City</p>
      <ul class="contact-list">
        <li>
          <svg viewBox="0 0 24 24" aria-hidden="true"><path d="M6.6 10.8a15 15 0 0 0 6.6 6.6l2.2-2.2c.3-.3.7-.4 1-.2 1.1.4 2.3.6 3.6.6.6 0 1 .4 1 1V20c0 .6-.4 1-1 1A17 17 0 0 1 3 4c0-.6.4-1 1-1h3.5c.6 0 1 .4 1 1 0 1.3.2 2.5.6 3.6.1.3 0 .7-.2 1z"/></svg>
          123 456 789
        </li>
        <li>
          <svg viewBox="0 0 24 24" aria-hidden="true"><path d="M2 5h20v14H2zm2 2v.5l8 5 8-5V7l-8 5z"/></svg>
          info@brightmoorcardco.com
        </li>
        <li>
          <svg viewBox="0 0 24 24" aria-hidden="true"><circle cx="12" cy="12" r="10"/></svg>
          www.brightmoorcardco.com
        </li>
      </ul>
    </div>
  </section>
</main>
</body>
</html>
```